custom carpentry, woodworking and home repair company needs logo design and business card design

Attention: I apologize but I just received notification from my state that I cannot use the company name that I originally submitted (Beyond The Bench). The new name will be Joinolux We need a company logo and business card design for our new company based in the Hampton Roads area of Virginia. The company name is Joinolux. The final design should give a first impression of true craftsmanship and attention to detail. We would like the card to include the company name, my name Mark Tellman (owner), phone number (757) 348-2615, website (joinolux-example.com) and email address (mark@joinolux-example.com). Everything else is up to your discretion. Thanks, have fun, and good luck.

Industry/Entity Type

Business

Contact Information for Business Card

See project description

Logo Text

see project description

Colors

Designer to choose colors to be used in the design.

```html
<!DOCTYPE html>
<html lang="en">
<head>
<meta charset="utf-8">
<title>Joinolux Business Card</title>
<link rel="stylesheet" href="https://fonts.googleapis.com/css2?family=Open+Sans:wght@300;400;500&display=swap">
<style>
  :root {
    --bg: #e5e5e5;
    --ink: #22222f;
    --gold: #fdb93a;
    --amber: #d08a2c;
    --walnut: #8b5c19;
    --paper: #f1f1f1;
    --white: #ffffff;
    --black: #111111;
  }
  html, body {
    margin: 0;
    padding: 0;
    width: 1200px;
    height: 1200px;
    overflow: hidden;
    background: var(--bg);
  }
  .canvas {
    display: block;
    width: 1200px;
    height: 1200px;
    font-family: "Open Sans", sans-serif;
  }
  .card-base { fill: var(--ink); }
  .band-paper { fill: var(--paper); }
  .band-gold { fill: var(--gold); }
  .band-amber { fill: var(--amber); }
  .band-walnut { fill: var(--walnut); }
  .brand-dot { fill: var(--amber); }
  .brand-name {
    fill: var(--gold);
    font-weight: 400;
    font-size: 28px;
    letter-spacing: 0.5px;
  }
  .back-brand-name {
    fill: var(--amber);
    font-weight: 400;
    font-size: 26px;
    letter-spacing: 0.5px;
  }
  .front-title {
    fill: var(--white);
    font-weight: 400;
    font-size: 74px;
    letter-spacing: 1px;
  }
  .holder-name {
    fill: var(--black);
    font-weight: 400;
    font-size: 56px;
  }
  .contact-text {
    fill: var(--ink);
    font-weight: 400;
    font-size: 23px;
  }
  .icon-disc { fill: var(--ink); }
  .icon-line {
    fill: none;
    stroke: var(--white);
    stroke-width: 2;
    stroke-linejoin: round;
  }
  .icon-fill { fill: var(--white); }
</style>
</head>
<body>
<svg class="canvas" viewBox="0 0 1500 1500" xmlns="http://www.w3.org/2000/svg">

  <g class="corner-brand">
    <circle class="brand-dot" cx="100" cy="120" r="26"/>
    <text class="brand-name" x="138" y="128">Joinolux</text>
  </g>

  <g class="card-front">
    <rect class="card-base" x="318" y="180" width="882" height="490"/>
    <polygon class="band-paper" points="760,550 1200,462 1200,640"/>
    <polygon class="band-gold" points="318,462 1200,640 1200,670 318,670"/>
    <polygon class="band-amber" points="318,515 1070,670 318,670"/>
    <polygon class="band-walnut" points="318,565 820,670 318,670"/>

    <g class="front-brand">
      <circle class="brand-dot" cx="700" cy="310" r="24"/>
      <text class="brand-name" x="740" y="320">Joinolux</text>
    </g>
    <text class="front-title" x="766" y="462" text-anchor="middle">JOINOLUX</text>
  </g>

  <g class="card-back">
    <rect class="card-base" x="318" y="778" width="882" height="490"/>
    <polygon class="band-paper" points="690,778 912,778 1092,1268 870,1268"/>
    <polygon class="band-gold" points="912,778 988,778 1168,1268 1092,1268"/>
    <polygon class="band-amber" points="988,778 1063,778 1200,1140 1200,1268 1168,1268"/>
    <polygon class="band-walnut" points="1063,778 1200,778 1200,1140"/>

    <g class="back-brand">
      <circle class="brand-dot" cx="905" cy="1080" r="26"/>
      <text class="back-brand-name" x="915" y="1120" transform="rotate(62 915 1120)">Joinolux</text>
    </g>

    <g class="name-banner">
      <polygon class="band-walnut" points="737,903 790,903 750,945"/>
      <polygon class="band-gold" points="318,820 760,820 790,903 318,903"/>
      <text class="holder-name" x="338" y="884" textLength="412" lengthAdjust="spacingAndGlyphs">MARK TELLMAN</text>
    </g>

    <g class="contact-row contact-email">
      <path class="band-gold" d="M318 952 H702 a35 35 0 0 1 0 69 H318 Z"/>
      <circle class="icon-disc" cx="357" cy="987" r="18"/>
      <rect class="icon-line" x="347" y="980" width="20" height="14"/>
      <polyline class="icon-line" points="347,980 357,988 367,980"/>
      <text class="contact-text" x="388" y="995">mark@joinolux-example.com</text>
    </g>

    <g class="contact-row contact-web">
      <path class="band-amber" d="M318 1038 H702 a35 35 0 0 1 0 69 H318 Z"/>
      <circle class="icon-disc" cx="357" cy="1073" r="18"/>
      <circle class="icon-line" cx="357" cy="1073" r="10"/>
      <ellipse class="icon-line" cx="357" cy="1073" rx="4" ry="10"/>
      <line class="icon-line" x1="347" y1="1073" x2="367" y2="1073"/>
      <text class="contact-text" x="388" y="1081">joinolux-example.com</text>
    </g>

    <g class="contact-row contact-phone">
      <path class="band-walnut" d="M318 1125 H702 a35 35 0 0 1 0 69 H318 Z"/>
      <circle class="icon-disc" cx="357" cy="1159" r="18"/>
      <path class="icon-fill" d="M349 1149 l5 -2 l4 7 l-3 3 q3 6 9 9 l3 -3 l7 4 l-2 5 q-12 2 -20 -8 q-6 -8 -3 -15 Z"/>
      <text class="contact-text" x="388" y="1167">(757) 348-2615</text>
    </g>
  </g>
</svg>
</body>
</html>
```